Company corporate advertising sign and banner for different uses

Hello,
We are a handcraft business and in need of an advertising sign and banner for different uses based on our company logo.
The banner should be usable mainly for advertising on different websites and as this we think it should be in landscape format.
The advertising sign should be usable in different sizes. Firstly we would need it in 50cmx60cm or similar format, so we can let it print on plexiglas or as a plastic sign (and similar) to screw it on a wall near our company so people (mainly delivery companies) are able to find our warehouse on the other side we would need this same sign in plastic or perhaps thin metal to put it as an advertising and contact sign on our different projects that we are realizing, for example car barriers, video surveillance systems, alarm systems for home or company use (outside on the sirenes), on electric boxes like car charging stations, computers and much other things, so you see the very need that we must be able to change the size of the advertising sign but it must still be recognizable that our company realized that sort of work.
We have a logo that must be represented on that sign and also our company details must be present, so people are able to contact us.
The advertising sign and the banner should go hand in hand, so that everyone can recognize on first sight that it is our company.
We put our logo in the upload files section, the text on the right side of the logo can be used but is not an absolute must, depends on the ideas of the design and the designer.
The text we absolutely would need is beside our phone, website address and email address which are :
+352 26417958
www.dorvelmask.lu
info@dorvelmask.lu
the following text, representing our services :
Réparations et rénovations tout genre
Electricité générale, dépannages, domotique, systèmes d'alarme et de vidéosurveillance
Solutions et services en informatique
Aménagements de l'extérieur, services de jardinage
Thanks very much
Target Market(s)
private and business customers
Industry/Entity Type
craft business

```html
<!DOCTYPE html>
<html lang="fr">
<head>
<meta charset="utf-8">
<title>Dorvelmask – panneau publicitaire</title>
<link rel="stylesheet" href="https://fonts.googleapis.com/css2?family=Oswald:wght@500&family=Fraunces:opsz,wght@72,600&family=Poppins:wght@400;600&display=swap">
<style>
  :root {
    --navy: #221a38;
    --orange: #f7ad45;
    --white: #ffffff;
  }
  * { margin: 0; padding: 0; box-sizing: border-box; }
  html, body { width: 1000px; height: 1200px; overflow: hidden; background: var(--white); }
  .sign { position: relative; width: 1000px; height: 1200px; background: var(--white); }
  .header-art { position: absolute; left: 0; top: 0; width: 1000px; height: 381px; }
  .brand {
    position: absolute; left: 462px; top: 120px;
    font-family: "Poppins", sans-serif; font-weight: 600;
    color: var(--navy); font-size: 46px; letter-spacing: 2px; line-height: 1;
    text-transform: uppercase;
  }
  .tagline {
    position: absolute; left: 535px; top: 180px;
    font-family: "Poppins", sans-serif; font-weight: 400;
    color: var(--navy); font-size: 25px; line-height: 1;
  }
  .phone {
    position: absolute; left: 455px; top: 240px;
    display: flex; align-items: center; gap: 10px;
    font-family: "Oswald", sans-serif; font-weight: 500;
    color: var(--orange); font-size: 64px; line-height: 1;
  }
  .phone svg { width: 44px; height: 44px; }
  .services { position: absolute; left: 36px; top: 488px; width: 940px; list-style: none; }
  .service {
    position: relative; padding-left: 70px;
    font-family: "Fraunces", serif; font-weight: 600;
    color: var(--navy); font-size: 40px; line-height: 48px;
  }
  .service + .service { margin-top: 53px; }
  .service::before {
    content: ""; position: absolute; left: 4px; top: 3px;
    width: 40px; height: 40px; border-radius: 50%;
    border: 3px solid var(--navy); background: var(--orange);
    box-shadow: inset 0 0 0 4px var(--white);
  }
  .footer {
    position: absolute; left: 0; top: 1057px; width: 1000px; height: 107px;
    background: var(--navy); display: flex; align-items: center;
    font-family: "Fraunces", serif; font-weight: 400; color: var(--orange); font-size: 33px;
  }
  .contact { position: absolute; display: flex; align-items: center; gap: 14px; }
  .contact.web { left: 42px; }
  .contact.mail { left: 534px; }
  .contact svg { width: 42px; height: 42px; }
</style>
</head>
<body>
<div class="sign">
  <svg class="header-art" viewBox="0 0 1000 381" aria-hidden="true">
    <rect x="0" y="0" width="1000" height="381" fill="var(--orange)"/>
    <rect x="0" y="0" width="1000" height="14" fill="var(--navy)"/>
    <path d="M293 14 H1000 V346 H295 L182 278 Q156 262 156 232 V110 Q156 82 182 70 Z" fill="var(--white)"/>
    <path d="M360 233 H1000 V321 H342 Q334 321 338 314 L350 240 Q352 233 360 233 Z" fill="var(--navy)"/>
    <circle cx="303" cy="180" r="118" fill="var(--navy)"/>
  </svg>

  <div class="brand">Dorvelmask</div>
  <div class="tagline">dee (bal) alles kann</div>

  <div class="phone">
    <svg viewBox="0 0 24 24" aria-hidden="true"><path fill="var(--orange)" d="M6.6 10.8a15.1 15.1 0 0 0 6.6 6.6l2.2-2.2a1 1 0 0 1 1-.25 11.4 11.4 0 0 0 3.6.57 1 1 0 0 1 1 1V20a1 1 0 0 1-1 1A17 17 0 0 1 3 4a1 1 0 0 1 1-1h3.5a1 1 0 0 1 1 1c0 1.25.2 2.45.57 3.57a1 1 0 0 1-.25 1z"/></svg>
    <span>+352 26417958</span>
  </div>

  <ul class="services">
    <li class="service">Réparations et rénovations tout genre</li>
    <li class="service">Electricité générale, dépannages,<br>domotique, systèmes d’alarme et de<br>vidéosurveillance</li>
    <li class="service">Solutions et services en informatique</li>
    <li class="service">Aménagements de l’extérieur, services<br>de jardinage</li>
  </ul>

  <div class="footer">
    <div class="contact web">
      <svg viewBox="0 0 24 24" aria-hidden="true" fill="none" stroke="var(--orange)" stroke-width="1.6"><circle cx="12" cy="12" r="10"/><ellipse cx="12" cy="12" rx="4.5" ry="10"/><path d="M2 12h20M3.5 7h17M3.5 17h17"/></svg>
      <span>www.dorvelmask.lu</span>
    </div>
    <div class="contact mail">
      <svg viewBox="0 0 24 24" aria-hidden="true" fill="none" stroke="var(--orange)" stroke-width="1.8"><rect x="2" y="5" width="20" height="14"/><path d="M2 5l10 8 10-8M2 19l7.5-7M22 19l-7.5-7"/></svg>
      <span>info@dorvelmask.lu</span>
    </div>
  </div>
</div>
</body>
</html>
```